Financial Planning Business needs a business card design

We need a business card design that is for a new financial planning business based in Australia. We provide financial planning advice such as retirement planning, wealth creation, asset protection.

Attached is the logo design. On the front side of the business card needs to incorporate the following:
- adviser name
- adviser title (ie Managing Director)
- address
- phone number
- email
- website address

Ideally it should also have the business name and logo

On the back of the card I would like this to be black in colour with the business name and logo

I have been advised the font is "Cinzel" (regular and bold)

Industry/Entity Type

Financial

Requirements
Must have
• Logo and business name

Format to have as follows:
Tom Harlowe
Managing Director / Senior Financial Adviser
address
phone email
website

```html
<!DOCTYPE html>
<html lang="en">
<head>
<meta charset="utf-8">
<title>Keelan Wealth Planning – Business Cards</title>
<link href="https://fonts.googleapis.com/css2?family=Cinzel:wght@400;700&display=swap" rel="stylesheet">
<style>
  :root {
    --stage: #1b1b1b;
    --card-dark: #262626;
    --card-white: #ffffff;
    --panel-dark: #3a3a3a;
    --panel-grey: #a9aaac;
    --brand-blue: #1d9ad6;
    --brand-grey: #9c9c9c;
    --text-light: #d6d6d6;
    --text-muted: #9a9a9a;
  }
  * { box-sizing: border-box; margin: 0; padding: 0; }
  html, body {
    width: 1200px; height: 1000px; overflow: hidden;
    background: var(--stage);
    font-family: "Cinzel", serif;
  }
  .stage {
    width: 1200px; height: 1000px;
    display: flex; align-items: center; justify-content: center; gap: 60px;
  }
  .card {
    position: relative;
    width: 540px; height: 310px;
    overflow: hidden;
    box-shadow: 0 18px 40px rgba(0,0,0,0.55);
  }

  /* Back of card */
  .card--back { background: var(--card-dark); }
  .back-brand {
    position: absolute; left: 70px; top: 92px;
    display: flex; align-items: center; gap: 18px;
    color: var(--brand-blue);
  }
  .brand-square { width: 46px; height: 46px; background: var(--brand-blue); }
  .brand-name { display: block; line-height: 1; font-weight: 400; }
  .brand-name__main { display: block; font-size: 58px; letter-spacing: 1px; }
  .brand-name__sub { display: block; font-size: 21px; letter-spacing: 1.5px; margin-top: 4px; text-align: right; }
  .back-web {
    position: absolute; left: 0; right: 0; top: 222px;
    text-align: center; font-size: 13px; letter-spacing: 4px;
    color: var(--text-muted);
  }

  /* Front of card */
  .card--front { background: var(--card-white); }
  .front-shapes { position: absolute; inset: 0; }
  .contact {
    position: absolute; left: 40px; top: 30px;
    color: var(--text-light);
  }
  .contact__name { font-weight: 700; font-size: 16px; color: var(--brand-blue); letter-spacing: 1px; }
  .contact__title { font-size: 10px; margin-top: 3px; letter-spacing: 0.5px; }
  .contact__line { font-size: 10px; margin-top: 4px; }
  .contact__line--first { margin-top: 16px; }
  .front-web {
    position: absolute; left: 30px; top: 214px;
    font-size: 10px; color: #ffffff; letter-spacing: 0.5px;
  }
  .address {
    position: absolute; left: 150px; top: 250px;
    font-size: 10px; line-height: 1.45; color: var(--text-light);
    font-style: normal;
  }
  .front-brand {
    position: absolute; left: 310px; top: 112px;
    color: var(--brand-blue);
  }
  .front-brand .brand-name__main { font-size: 40px; }
  .front-brand .brand-name__sub { font-size: 14px; letter-spacing: 1px; }
</style>
</head>
<body>
<main class="stage">

  <section class="card card--back" aria-label="Card back">
    <div class="back-brand">
      <span class="brand-square"></span>
      <span class="brand-name">
        <span class="brand-name__main">KEELAN</span>
        <span class="brand-name__sub">WEALTH PLANNING</span>
      </span>
    </div>
    <p class="back-web">WWW.KEELANWEALTH.COM</p>
  </section>

  <section class="card card--front" aria-label="Card front">
    <svg class="front-shapes" width="540" height="310" viewBox="0 0 540 310" aria-hidden="true">
      <polygon points="14,14 255,14 272,296 125,296 150,240 14,240" fill="var(--panel-dark)"/>
      <polygon points="14,150 190,165 150,240 14,240" fill="var(--panel-grey)"/>
    </svg>

    <div class="contact">
      <p class="contact__name">TOM HARLOWE</p>
      <p class="contact__title">MANAGING DIRECTOR</p>
      <p class="contact__line contact__line--first">+61 2 4000 1234</p>
      <p class="contact__line">TOM@KEELANWEALTH.COM</p>
    </div>

    <p class="front-web">WWW.KEELANWEALTH.COM</p>

    <address class="address">
      12 HARBOUR LANE<br>
      CORAL BAY NORTH.<br>
      TEL + 61 7 5500 0000
    </address>

    <div class="front-brand">
      <span class="brand-name">
        <span class="brand-name__main">KEELAN</span>
        <span class="brand-name__sub">WEALTH PLANNING</span>
      </span>
    </div>
  </section>

</main>
</body>
</html>
```